Letterhead Design Project

I need letterhead designed for my law firm. It would also be used for web based stuff as well.

Industry/Entity Type

Law Firm

```html
<!DOCTYPE html>
<html lang="en">
<head>
<meta charset="utf-8">
<title>Harlow &amp; Mercer Law Firm Letterhead</title>
<link rel="stylesheet" href="https://fonts.googleapis.com/css2?family=Arimo:wght@400;700&family=Noto+Sans:wght@400&display=swap">
<style>
  :root {
    --paper: #ffffff;
    --accent: #0a84b4;
    --ink: #2a2a2a;
    --footer-ink: #1f3550;
  }
  * { margin: 0; padding: 0; box-sizing: border-box; }
  html, body {
    width: 848px;
    height: 1200px;
    overflow: hidden;
    background: var(--paper);
  }
  .letterhead {
    position: relative;
    width: 848px;
    height: 1200px;
    background: var(--paper);
  }
  .firm-name {
    position: absolute;
    left: 18px;
    top: 34px;
    font-family: "Arimo", sans-serif;
    font-weight: 700;
    font-size: 27px;
    letter-spacing: 0.5px;
    text-transform: uppercase;
    color: var(--ink);
    white-space: nowrap;
  }
  .rule {
    position: absolute;
    height: 5px;
    background: var(--accent);
  }
  .rule--header-top { left: 0; top: 71px; width: 567px; }
  .rule--header-tagline { left: 271px; top: 101px; width: 577px; }
  .rule--footer { left: 0; top: 1170px; width: 185px; }
  .firm-tagline {
    position: absolute;
    left: 168px;
    top: 93px;
    font-family: "Arimo", sans-serif;
    font-weight: 400;
    font-size: 16px;
    color: var(--ink);
    white-space: nowrap;
  }
  .contact-line {
    position: absolute;
    right: 12px;
    top: 1163px;
    font-family: "Noto Sans", sans-serif;
    font-size: 14.5px;
    color: var(--footer-ink);
    white-space: nowrap;
  }
</style>
</head>
<body>
  <div class="letterhead">
    <header class="letterhead-header">
      <div class="firm-name">Harlow &amp; Mercer</div>
      <div class="rule rule--header-top"></div>
      <div class="firm-tagline">LAW FIRM</div>
      <div class="rule rule--header-tagline"></div>
    </header>
    <footer class="letterhead-footer">
      <div class="rule rule--footer"></div>
      <p class="contact-line">Phone:55555555/Fax:5555555/5555street address,city, state/webaddress.com</p>
    </footer>
  </div>
</body>
</html>
```